Medical Waste Company with Logo

Need a business card design that targets office managers in the medical community. This card will be the front line for our sales team to market our services to the community. We would like to have email, phone number, website. Please use the logo attached to create a design that we would be proud of.

Target Market(s)

Medical Clients

Industry/Entity Type

Medical Supply

Contact Information for Business Card

Please use logo attached

Colors

Designer to choose colors to be used in the design.

Requirements
Must have
• Our logo (see attached file)
Nice to have
• Maybe a pop of some sort, raised..?

```html
<!DOCTYPE html>
<html lang="en">
<head>
<meta charset="utf-8">
<title>Northpeak Clinical Waste – Business Card</title>
<link href="https://fonts.googleapis.com/css2?family=Roboto:wght@400;500;700&display=swap" rel="stylesheet">
<style>
  :root {
    --stage: #2b2e33;
    --card-white: #ffffff;
    --panel-grey: #f1f2f4;
    --divider-grey: #9a9da2;
    --brand-blue: #1f6fae;
    --text-dark: #2a2d31;
    --text-grey: #55595f;
    --card-black: #1c1b1c;
    --silver: #c9cbce;
  }
  * { margin: 0; padding: 0; box-sizing: border-box; }
  html, body {
    width: 1200px; height: 900px; overflow: hidden;
    background: var(--stage);
    font-family: 'Roboto', Arial, sans-serif;
  }
  .stage {
    width: 1200px; height: 900px;
    display: flex; align-items: center; justify-content: center; gap: 40px;
  }
  .card {
    position: relative;
    width: 540px; height: 310px;
    border-radius: 22px;
    overflow: hidden;
  }
  .card-front { background: var(--card-white); }
  .card-front .shapes { position: absolute; inset: 0; }
  .contact-block {
    position: absolute; left: 34px; top: 32px;
    color: var(--text-dark);
  }
  .employee-name {
    color: var(--brand-blue);
    font-weight: 500; font-size: 22px; letter-spacing: 0.2px;
  }
  .employee-role {
    font-size: 11px; color: var(--text-grey); margin-top: 2px;
  }
  .contact-list { list-style: none; margin-top: 22px; }
  .contact-list li {
    display: flex; align-items: center; gap: 9px;
    font-size: 12.5px; margin-bottom: 6px;
  }
  .contact-list svg { width: 12px; height: 12px; flex: none; }
  .address { font-size: 12.5px; line-height: 1.45; margin-top: 14px; }
  .front-brand {
    position: absolute; left: 276px; top: 262px;
    font-weight: 700; font-size: 20px; letter-spacing: 1px;
    color: var(--divider-grey);
  }
  .card-back {
    background: var(--card-black);
    display: flex; align-items: center; justify-content: center;
  }
  .back-brand {
    text-align: center;
    color: var(--silver);
    font-weight: 700; font-size: 30px; line-height: 1.25; letter-spacing: 2px;
  }
</style>
</head>
<body>
<main class="stage">
  <section class="card card-front">
    <svg class="shapes" viewBox="0 0 540 310" aria-hidden="true">
      <polygon points="190,310 540,70 540,310" fill="var(--panel-grey)"/>
      <line x1="190" y1="310" x2="540" y2="70" stroke="var(--divider-grey)" stroke-width="5"/>
      <polygon points="400,310 540,120 540,310" fill="var(--brand-blue)"/>
      <line x1="400" y1="310" x2="540" y2="120" stroke="var(--divider-grey)" stroke-width="4"/>
    </svg>
    <div class="contact-block">
      <h1 class="employee-name">EMPLOYEE NAME</h1>
      <p class="employee-role">MANAGER</p>
      <ul class="contact-list">
        <li>
          <svg viewBox="0 0 24 24"><path fill="var(--brand-blue)" d="M6.6 10.8a15 15 0 0 0 6.6 6.6l2.2-2.2c.3-.3.7-.4 1-.2 1.1.4 2.3.6 3.6.6.6 0 1 .4 1 1V20c0 .6-.4 1-1 1A17 17 0 0 1 3 4c0-.6.4-1 1-1h3.5c.6 0 1 .4 1 1 0 1.3.2 2.5.6 3.6.1.3 0 .7-.2 1z"/></svg>
          03 5550 1842
        </li>
        <li>
          <svg viewBox="0 0 24 24"><path fill="var(--brand-blue)" d="M2 5h20v14H2zm2 2v.5l8 5 8-5V7z"/></svg>
          EMAILADDRESS@DOMAIN.COM
        </li>
        <li>
          <svg viewBox="0 0 24 24"><circle cx="12" cy="12" r="9" fill="none" stroke="var(--brand-blue)" stroke-width="2"/><path d="M3 12h18M12 3c3 3 3 15 0 18M12 3c-3 3-3 15 0 18" fill="none" stroke="var(--brand-blue)" stroke-width="1.6"/></svg>
          WWW.NORTHPEAKCLINICALWASTE.COM
        </li>
      </ul>
      <p class="address">LEVEL 4, 27 HARBOUR ROAD<br>PLACE NAME</p>
    </div>
    <p class="front-brand">NORTHPEAK</p>
  </section>

  <section class="card card-back">
    <p class="back-brand">NORTHPEAK<br>CLINICAL WASTE</p>
  </section>
</main>
</body>
</html>
```